Power Point Template for a Construction & Interior design Company for proposal submission.

We are a construction and Interior Design company who have recently rebranded. We have designed a new logo and are now looking to create Word and PowerPoint templates for the submission of our proposals and property information packs. We will need to ensure that we have the right graphics and symbols on the relevant pages. We would like to standardise our approach by inserting a symbol reflecting the title of the page for each of the pages. So for example, if the page title is Costings we have a symbol highlighting the work "Costings" in the top corner of that page. the same design approach will be followed for each of the pages.
We will need the following pages
1. Cover Page - we would like to standardise this for all our quotes, property information packs and general company presentation. So, we will have 3 cover page versions with relevant images as follows:
Cover Page - Project Proposal
Cover Page - Property Information Pack
Cover - Company Info.
2. Company Overview - Please use the aligned imagery of this page.
3. The Team
4. portfolio of projects - This will be a gallery of images showcasing our projects with a small write-up about the property. We will have 2 pages for this section.
5. Scope of works - This will be a section where we will insert an excel sheet as an object into the PP slide to list out the costings of all the relevant tasks. Will need to add the relevant imagery and symbols for the following section such as:
Foundations
Brickwork
Drywalling
Plumbing
Heating
Bathrooms
Tiling
Joinery
Roof
Exterior Landscape
Smart Automation
CCTV
Burglar Alarm
Decorative lights
Windows
Wall Paper
Paint
This section could span multiple pages so we will need the ability to duplicate the slides and insert the relevant imagery and symbols for the various sections.
6. Project Delivery Timeline - We need the timeline infographic here and the ability to add an excel sheet containing the project delivery timeline.
7. Project Costs - 2 options required here please:
Either we enter the costs of the project directly on the PP slide so need one slide for this and the other option will be to insert a costing Excel sheet here.
8. Terms & Conditions - Insert a word file or prepare multiple slides containing our T & C's.
Cover Page for Property Pack
Opportunity Overview - page to summarise the investment opp.
Investment Strategies - Page to explain the investment viability and the potential return on investment.
Plane & images - Page to show the floor plans and images of any property.
Planning - Page to show the planning approval obtained for the said property.
Comparable - Page to show the value and details of similar properties within the same catchment area. Here the content will be text, Images and links.
Risk warning - waiver page
The idea is that once this template is created, we can standardise our branding for all customer communications and will use this template to submit
Property building and design proposal
Property Information packs
Std. company information.

Target Market(s)

High net worth individuals looking to build and design luxury properties and buy investment property.

Industry/Entity Type

Construction, interior design, property investors, real estate.

Requirements
Must have
• Continuity of brand from our Logo and across all types of customer communication. Must have symbols on each page reflecting the title of the slide. Aligned imagery and not just random ones. Use of infographics on various pages which. .
Nice to have
• Footer on each page stating our contact details and SM media links. Page numbers.

```html
<!DOCTYPE html>
<html lang="en">
<head>
<meta charset="utf-8">
<title>Veridane &amp; Co – Proposal Template</title>
<link href="https://fonts.googleapis.com/css2?family=Rubik:wght@500;600&family=Poppins:wght@300;400;500;600&display=swap" rel="stylesheet">
<style>
:root{
  --teal:#2d7865;
  --teal-dark:#235f50;
  --teal-mid:#5a9a89;
  --teal-soft:#9cc4b8;
  --teal-light:#4fb3a6;
  --ink:#1d1d1d;
  --body:#3a3a3a;
  --stage:#c9c9c9;
  --band:#ebebeb;
  --white:#ffffff;
}
*{box-sizing:border-box;margin:0;padding:0}
html,body{width:1200px;height:4283px;overflow:hidden}
body{background:var(--stage);font-family:"Poppins",sans-serif;color:var(--body);position:relative}
.slide{position:absolute;left:23px;width:1153px;height:648px;background:var(--white);overflow:hidden}
.abs{position:absolute}
.photo{position:absolute}
.title{font-family:"Rubik",sans-serif;font-weight:600;color:var(--teal);letter-spacing:.3px}
.title--center{left:0;width:100%;text-align:center;font-size:34px}
.para{font-size:12px;line-height:20px;color:var(--body)}
.brand{position:absolute;display:flex;align-items:center;gap:10px}
.brand__mark{width:56px;height:56px;border-radius:50%;border:3px solid var(--teal)}
.brand__name{font-family:"Rubik",sans-serif;font-weight:600;font-size:16px;color:var(--teal);letter-spacing:1px}
.page-icon{position:absolute;width:74px;height:74px;border-radius:50%;background:var(--teal);display:flex;align-items:center;justify-content:center}
.marker{position:absolute;left:0;width:0;height:0;border-top:14px solid transparent;border-bottom:14px solid transparent;border-left:16px solid var(--teal)}
.footer-band{position:absolute;left:0;bottom:0;width:100%;height:53px;background:var(--band)}
.steps{position:absolute;left:0;bottom:0}
.page-no{position:absolute;right:0;bottom:0;background:var(--teal);color:var(--white);font-family:"Rubik",sans-serif;font-weight:500;font-size:20px;display:flex;justify-content:center}
.social{position:absolute;display:flex;gap:20px}
.social span{width:18px;height:18px;border-radius:50%;background:var(--ink)}
.phone{position:absolute;display:flex;align-items:center;gap:6px;font-size:15px;font-weight:500;color:var(--ink)}
/* cover */
.cover__card{position:absolute;left:20px;top:28px;width:549px;height:593px;background:var(--white)}
.cover__tab{position:absolute;left:20px;top:28px;width:158px;height:30px;background:var(--teal)}
.cover__block{position:absolute;left:587px;top:322px;width:533px;height:299px;background:var(--teal)}
.cover__welcome{position:absolute;left:20px;width:549px;text-align:center;font-weight:600;color:var(--ink)}
/* team */
.member__photo{position:absolute;width:152px;height:152px;border-radius:50%;background:linear-gradient(160deg,#d9d2c8,#7b6d61)}
.member__name{position:absolute;font-family:"Rubik",sans-serif;font-weight:600;font-size:19px;color:var(--ink)}
.member__bio{position:absolute;width:232px;font-size:10.5px;line-height:17px;text-align:justify;color:#555}
/* portfolio */
.gallery__img{position:absolute;top:213px;width:329px;height:207px}
.gallery__caption{position:absolute;top:430px;width:329px;height:134px;background:var(--teal);color:var(--white);font-size:15px;line-height:22px;text-align:center;display:flex;align-items:center;justify-content:center;padding:0 30px}
/* scope */
.scope__col{position:absolute;top:175px;width:326px}
.scope__head{text-align:center;font-family:"Rubik",sans-serif;font-weight:600;font-size:19px;color:var(--teal);height:24px}
.scope__img{margin-top:0;height:218px}
.scope__table{margin-top:15px;background:var(--teal);padding:10px 12px}
.scope__table table{width:100%;border-collapse:collapse;background:var(--white);font-size:17px;color:var(--ink)}
.scope__table th,.scope__table td{border:2px solid var(--ink);padding:1px 5px;text-align:left;white-space:nowrap}
.scope__table th{font-weight:600;font-size:16px}
/* timeline */
.timeline__name{position:absolute;font-size:32px;font-weight:300}
</style>
</head>
<body>

<!-- Slide 1: Cover -->
<section class="slide" style="top:75px">
  <div class="photo" role="img" aria-label="Warm beige interior with curved sofa and paper pendant lamp" style="left:0;top:0;width:1153px;height:648px;background:linear-gradient(135deg,#8a7563,#c4b3a1 45%,#9a8a7a)"></div>
  <div class="cover__card"></div>
  <div class="cover__tab"></div>
  <div class="cover__block"></div>
  <div class="photo" role="img" aria-label="Living room with cream curved sofa, round coffee table and paper globe pendant" style="left:647px;top:60px;width:420px;height:528px;background:linear-gradient(180deg,#d8d3cc,#c3bbb1 60%,#9d948a)"></div>
  <div class="abs" style="left:257px;top:132px;width:88px;height:88px;border-radius:50%;border:3px solid var(--teal)"></div>
  <div class="abs title" style="left:20px;top:232px;width:549px;text-align:center;font-size:30px;color:var(--ink);font-weight:500;letter-spacing:2px">VERIDANE &amp; CO</div>
  <div class="cover__welcome" style="top:355px;font-size:15px">WELCOME TO</div>
  <div class="cover__welcome" style="top:372px;font-size:34px;font-family:'Rubik',sans-serif;font-weight:600">VERIDANE &amp; CO</div>
  <p class="para abs" style="left:101px;top:433px;width:404px;text-align:center;font-size:11.5px;line-height:19px">Lorem ipsum dolor sit amet, consectetur adipiscing elit, sed do eiusmod tempor incididunt ut labore et dolore magna aliqua. Quis ipsum suspendisse ultrices gravida. Risus commodo viverra maecenas accumsan lacus vel facilisis.</p>
  <div class="social" style="left:60px;top:564px"><span></span><span></span><span></span></div>
  <div class="phone" style="left:378px;top:561px"><svg width="14" height="14" viewBox="0 0 24 24"><path fill="#1d1d1d" d="M6.6 10.8a15 15 0 006.6 6.6l2.2-2.2c.3-.3.7-.4 1-.2 1.1.4 2.3.6 3.6.6.6 0 1 .4 1 1V20c0 .6-.4 1-1 1C10.6 21 3 13.4 3 4c0-.6.4-1 1-1h3.5c.6 0 1 .4 1 1 0 1.3.2 2.5.6 3.6.1.3 0 .7-.2 1z"/></svg>+(1) 555 014 2290</div>
</section>

<!-- Slide 2: Company Overview -->
<section class="slide" style="top:766px">
  <svg class="abs" style="left:0;top:0" width="1153" height="648" role="img" aria-label="Teal-walled lounge with sectional sofa and brass pendant lights">
    <defs><linearGradient id="ovg" x1="0" y1="0" x2="1" y2="1"><stop offset="0" stop-color="#5d8b8b"/><stop offset=".6" stop-color="#3f6f72"/><stop offset="1" stop-color="#5a4a3c"/></linearGradient></defs>
    <path d="M442,0 C470,120 720,150 680,330 C650,450 560,520 590,648 L1153,648 L1153,0 Z" fill="url(#ovg)"/>
  </svg>
  <div class="marker" style="top:70px"></div>
  <div class="brand" style="left:60px;top:55px"><div class="brand__mark"></div><div class="brand__name">VERIDANE</div></div>
  <h2 class="title abs" style="left:63px;top:214px;font-size:31px">COMPANY OVERVIEW</h2>
  <p class="para abs" style="left:63px;top:272px;width:395px">Lorem ipsum dolor sit amet, consectetur adipiscing elit, sed do eiusmod tempor incididunt ut labore et dolore magna aliqua. Quis ipsum suspendisse ultrices gravida. Risus commodo viverra maecenas accumsan lacus vel facilisis. Lorem ipsum dolor sit amet, consectetur adipiscing elit, sed do eiusmod tempor incididunt ut labore et dolore magna aliqua. Quis ipsum suspendisse ultrices gravida. Risus commodo viverra maecenas accumsan lacus vel facilisis. Lorem ipsum dolor sit amet, consectetur adipiscing elit, sed do eiusmod tempor incididunt ut labore et dolore magna aliqua. Quis ipsum suspendisse ultrices gravida. Risus commodo viverra maecenas accumsan lacus vel facilisis.</p>
  <div class="page-icon" style="left:1042px;top:31px"><svg width="32" height="32" viewBox="0 0 24 24" fill="none" stroke="#fff" stroke-width="1.6"><rect x="5" y="3" width="12" height="17" rx="1"/><path d="M8 8h6M8 11h6M8 14h3"/><circle cx="16" cy="17" r="3"/><path d="M18 19l2.5 2.5"/></svg></div>
  <div class="social" style="left:63px;top:565px"><span></span><span></span><span></span></div>
  <div class="phone" style="left:352px;top:562px"><svg width="14" height="14" viewBox="0 0 24 24"><path fill="#1d1d1d" d="M6.6 10.8a15 15 0 006.6 6.6l2.2-2.2c.3-.3.7-.4 1-.2 1.1.4 2.3.6 3.6.6.6 0 1 .4 1 1V20c0 .6-.4 1-1 1C10.6 21 3 13.4 3 4c0-.6.4-1 1-1h3.5c.6 0 1 .4 1 1 0 1.3.2 2.5.6 3.6.1.3 0 .7-.2 1z"/></svg>+(1) 555 014 2290</div>
  <svg class="steps" width="60" height="60"><rect x="0" y="0" width="20" height="60" fill="#2d7865"/><rect x="20" y="20" width="20" height="40" fill="#5a9a89"/><rect x="40" y="40" width="20" height="20" fill="#9cc4b8"/></svg>
  <div class="page-no" style="width:94px;height:113px;align-items:center">02</div>
</section>

<!-- Slide 3: Our Team -->
<section class="slide" style="top:1456px">
  <div class="marker" style="top:70px"></div>
  <div class="brand" style="left:45px;top:50px"><div class="brand__mark"></div><div class="brand__name">VERIDANE</div></div>
  <h2 class="title title--center abs" style="top:50px">OUR TEAM</h2>
  <div class="page-icon" style="left:1042px;top:33px"><svg width="34" height="34" viewBox="0 0 24 24" fill="#fff"><circle cx="12" cy="8" r="3"/><circle cx="5.5" cy="9.5" r="2.2"/><circle cx="18.5" cy="9.5" r="2.2"/><path d="M6.5 18c0-3 2.5-5 5.5-5s5.5 2 5.5 5z"/><path d="M1.5 18c0-2.3 1.7-4 4-4 .8 0 1.4.2 2 .5-1 1-1.7 2.2-1.8 3.5zM22.5 18c0-2.3-1.7-4-4-4-.8 0-1.4.2-2 .5 1 1 1.7 2.2 1.8 3.5z"/></svg></div>

  <div class="member__photo" role="img" aria-label="Portrait of team member Daniel Ward" style="left:80px;top:176px"></div>
  <div class="member__name" style="left:251px;top:194px">DANIEL WARD</div>
  <p class="member__bio" style="left:251px;top:226px">Lorem ipsum dolor sit amet, consectetur adipiscing elit, sed do eiusmod tempor incididunt ut labore et dolore magna aliqua. Risus viverra maecenas accumsan lacus vel facilisis.</p>

  <div class="member__photo" role="img" aria-label="Portrait of team member Maria" style="left:519px;top:176px;background:linear-gradient(160deg,#e6d9b8,#8a6a4a)"></div>
  <div class="member__name" style="left:691px;top:194px">MARIA</div>
  <p class="member__bio" style="left:691px;top:226px">Lorem ipsum dolor sit amet, consectetur adipiscing elit, sed do eiusmod tempor incididunt ut labore et dolore magna aliqua. Risus viverra maecenas accumsan lacus vel facilisis.</p>

  <div class="member__photo" role="img" aria-label="Portrait of team member Peter K" style="left:230px;top:382px;background:linear-gradient(160deg,#9a8c80,#2f2a27)"></div>
  <div class="member__name" style="left:402px;top:400px">PETER K</div>
  <p class="member__bio" style="left:402px;top:432px">Lorem ipsum dolor sit amet, consectetur adipiscing elit, sed do eiusmod tempor incididunt ut labore et dolore magna aliqua. Risus viverra maecenas accumsan lacus vel facilisis.</p>

  <div class="member__photo" role="img" aria-label="Portrait of team member Sophie" style="left:669px;top:382px;background:linear-gradient(160deg,#e2c3a8,#7c4a33)"></div>
  <div class="member__name" style="left:843px;top:400px">SOPHIE</div>
  <p class="member__bio" style="left:843px;top:432px">Lorem ipsum dolor sit amet, consectetur adipiscing elit, sed do eiusmod tempor incididunt ut labore et dolore magna aliqua. Risus viverra maecenas accumsan lacus vel facilisis.</p>

  <div class="footer-band"></div>
  <svg class="steps" width="60" height="60"><rect x="0" y="0" width="20" height="60" fill="#2d7865"/><rect x="20" y="20" width="20" height="40" fill="#5a9a89"/><rect x="40" y="40" width="20" height="20" fill="#9cc4b8"/></svg>
  <div class="social" style="left:100px;top:612px"><span></span><span></span><span></span></div>
  <div class="phone" style="left:889px;top:610px"><svg width="14" height="14" viewBox="0 0 24 24"><path fill="#1d1d1d" d="M6.6 10.8a15 15 0 006.6 6.6l2.2-2.2c.3-.3.7-.4 1-.2 1.1.4 2.3.6 3.6.6.6 0 1 .4 1 1V20c0 .6-.4 1-1 1C10.6 21 3 13.4 3 4c0-.6.4-1 1-1h3.5c.6 0 1 .4 1 1 0 1.3.2 2.5.6 3.6.1.3 0 .7-.2 1z"/></svg>+(1) 555 014 2290</div>
  <svg class="abs" style="right:39px;bottom:0" width="40" height="40"><rect x="0" y="20" width="20" height="20" fill="#cfe2dc"/><rect x="20" y="0" width="20" height="40" fill="#9cc4b8"/></svg>
  <div class="page-no" style="width:39px;height:61px;padding-top:12px">03</div>
</section>

<!-- Slide 4: Portfolio -->
<section class="slide" style="top:2146px">
  <div class="marker" style="top:70px"></div>
  <div class="brand" style="left:45px;top:50px"><div class="brand__mark"></div><div class="brand__name">VERIDANE</div></div>
  <h2 class="title title--center abs" style="top:92px">PORTFOLIO OF PROJECTS</h2>
  <p class="para abs" style="left:156px;top:153px;width:838px;text-align:center;font-size:11.5px;line-height:20px;color:var(--ink)">Lorem ipsum dolor sit amet, consectetur adipiscing elit, sed do eiusmod tempor incididunt ut labore et dolore magna aliqua. Quis ipsum suspendisse ultrices gravida. Risus commodo viverra maecenas accumsan lacus vel facilisis.</p>
  <div class="page-icon" style="left:1042px;top:33px"><svg width="32" height="32" viewBox="0 0 24 24" fill="none" stroke="#fff" stroke-width="1.6"><path d="M3 7h6l2 2h10v10H3z"/><path d="M3 7V5h6"/><rect x="7" y="12" width="10" height="5"/></svg></div>

  <div class="gallery__img" role="img" aria-label="Designers reviewing a 3D building model on screen" style="left:60px;background:linear-gradient(135deg,#e8e4df,#8a8f96 60%,#3d3f44)"></div>
  <div class="gallery__img" role="img" aria-label="Architectural sketch with a model house held in hand" style="left:411px;background:linear-gradient(135deg,#f2f2f2,#c9c3bb 60%,#8b6d52)"></div>
  <div class="gallery__img" role="img" aria-label="Dark lounge with red sofa and tropical plants" style="left:763px;background:linear-gradient(135deg,#3b4a3f,#2a2f2b 50%,#8a3b3b)"></div>
  <div class="gallery__caption" style="left:60px">Lorem ipsum dolor sit amet, consectetur adipiscing elit, sed do eiusmod tempor incididunt ut labore et dolore magna aliqua.</div>
  <div class="gallery__caption" style="left:411px">Lorem ipsum dolor sit amet, consectetur adipiscing elit, sed do eiusmod tempor incididunt ut labore et dolore magna aliqua.</div>
  <div class="gallery__caption" style="left:763px">Lorem ipsum dolor sit amet, consectetur adipiscing elit, sed do eiusmod tempor incididunt ut labore et dolore magna aliqua.</div>

  <div class="footer-band"></div>
  <svg class="steps" width="60" height="60"><rect x="0" y="0" width="20" height="60" fill="#2d7865"/><rect x="20" y="20" width="20" height="40" fill="#5a9a89"/><rect x="40" y="40" width="20" height="20" fill="#9cc4b8"/></svg>
  <div class="social" style="left:100px;top:612px"><span></span><span></span><span></span></div>
  <div class="phone" style="left:889px;top:610px"><svg width="14" height="14" viewBox="0 0 24 24"><path fill="#1d1d1d" d="M6.6 10.8a15 15 0 006.6 6.6l2.2-2.2c.3-.3.7-.4 1-.2 1.1.4 2.3.6 3.6.6.6 0 1 .4 1 1V20c0 .6-.4 1-1 1C10.6 21 3 13.4 3 4c0-.6.4-1 1-1h3.5c.6 0 1 .4 1 1 0 1.3.2 2.5.6 3.6.1.3 0 .7-.2 1z"/></svg>+(1) 555 014 2290</div>
  <svg class="abs" style="right:39px;bottom:0" width="40" height="40"><rect x="0" y="20" width="20" height="20" fill="#cfe2dc"/><rect x="20" y="0" width="20" height="40" fill="#9cc4b8"/></svg>
  <div class="page-no" style="width:39px;height:61px;padding-top:12px">04</div>
</section>

<!-- Slide 5: Scope of Works -->
<section class="slide" style="top:2836px">
  <div class="marker" style="top:70px"></div>
  <div class="brand" style="left:45px;top:50px"><div class="brand__mark"></div><div class="brand__name">VERIDANE</div></div>
  <h2 class="title title--center abs" style="top:81px">SCOPE OF WORKS</h2>
  <div class="page-icon" style="left:1042px;top:33px"><svg width="32" height="32" viewBox="0 0 24 24" fill="none" stroke="#fff" stroke-width="1.6"><rect x="3" y="7" width="18" height="12" rx="1.5"/><path d="M9 7V5h6v2M3 12h18M11 12v2h2v-2"/></svg></div>

  <div class="scope__col" style="left:66px">
    <div class="scope__head">FOUNDATIONS</div>
    <div class="scope__img" role="img" aria-label="Brick foundation walls under construction" style="background:linear-gradient(180deg,#cfd6d8,#b9674a 55%,#7d8a6a)"></div>
    <div class="scope__table"><table><tr><th>Particulars</th><th>Project</th><th>Project Date</th></tr><tr><td>House 1</td><td>79%</td><td>30-03-2022</td></tr><tr><td>House 1</td><td>79%</td><td>30-03-2022</td></tr></table></div>
  </div>
  <div class="scope__col" style="left:416px">
    <div class="scope__head">BRICKWORK</div>
    <div class="scope__img" role="img" aria-label="Bricklayer spreading mortar on a brick course" style="background:linear-gradient(160deg,#d9c9b5,#c4583a 55%,#8f3e28)"></div>
    <div class="scope__table"><table><tr><th>Particulars</th><th>Project</th><th>Project Date</th></tr><tr><td>House 1</td><td>79%</td><td>30-03-2022</td></tr><tr><td>House 1</td><td>79%</td><td>30-03-2022</td></tr></table></div>
  </div>
  <div class="scope__col" style="left:766px">
    <div class="scope__head">DRYWALLING</div>
    <div class="scope__img" role="img" aria-label="Worker plastering a drywall ceiling" style="background:linear-gradient(180deg,#e6e7e9,#b8bcc2 60%,#9aa0a8)"></div>
    <div class="scope__table"><table><tr><th>Particulars</th><th>Project</th><th>Project Date</th></tr><tr><td>House 1</td><td>79%</td><td>30-03-2022</td></tr><tr><td>House 1</td><td>79%</td><td>30-03-2022</td></tr></table></div>
  </div>

  <div class="footer-band"></div>
  <svg class="steps" width="60" height="60"><rect x="0" y="0" width="20" height="60" fill="#2d7865"/><rect x="20" y="20" width="20" height="40" fill="#5a9a89"/><rect x="40" y="40" width="20" height="20" fill="#9cc4b8"/></svg>
  <div class="social" style="left:100px;top:612px"><span></span><span></span><span></span></div>
  <div class="phone" style="left:889px;top:610px"><svg width="14" height="14" viewBox="0 0 24 24"><path fill="#1d1d1d" d="M6.6 10.8a15 15 0 006.6 6.6l2.2-2.2c.3-.3.7-.4 1-.2 1.1.4 2.3.6 3.6.6.6 0 1 .4 1 1V20c0 .6-.4 1-1 1C10.6 21 3 13.4 3 4c0-.6.4-1 1-1h3.5c.6 0 1 .4 1 1 0 1.3.2 2.5.6 3.6.1.3 0 .7-.2 1z"/></svg>+(1) 555 014 2290</div>
  <svg class="abs" style="right:39px;bottom:0" width="40" height="40"><rect x="0" y="20" width="20" height="20" fill="#cfe2dc"/><rect x="20" y="0" width="20" height="40" fill="#9cc4b8"/></svg>
  <div class="page-no" style="width:39px;height:61px;padding-top:12px">05</div>
</section>

<!-- Slide 6: Project Delivery Timeline -->
<section class="slide" style="top:3527px">
  <div class="marker" style="top:70px"></div>
  <div class="brand" style="left:45px;top:50px"><div class="brand__mark"></div><div class="brand__name">VERIDANE</div></div>
  <h2 class="title title--center abs" style="top:43px">PROJECT DELIVERY TIMELINE</h2>
  <div class="page-icon" style="left:1042px;top:33px"><svg width="34" height="34" viewBox="0 0 24 24" fill="none" stroke="#fff" stroke-width="1.5"><path d="M2 8h5l2 2-2 2H2zM9 14h5l2 2-2 2H9zM15 5h5l2 2-2 2h-5zM7 12v2h2M14 9h1"/></svg></div>

  <svg class="abs chart" style="left:0;top:0" width="600" height="600" viewBox="0 0 600 600">
    <g transform="scale(1.662) translate(-14,-2122)">
      <g stroke="#d6d6d6" stroke-width="1" vector-effect="non-scaling-stroke">
        <path vector-effect="non-scaling-stroke" d="M76 2236H310M76 2265H310M76 2291H310M76 2319H310M76 2344H310M76 2370H310M76 2396H310M76 2423H310"/>
        <path vector-effect="non-scaling-stroke" d="M98 2213V2446M124 2213V2446M150 2213V2446M176 2213V2446M202 2213V2446M228 2213V2446M254 2213V2446M280 2213V2446"/>
      </g>
      <path vector-effect="non-scaling-stroke" d="M76 2213V2446H310" fill="none" stroke="#1d1d1d" stroke-width="1.5"/>
      <g font-family="Poppins,sans-serif" font-size="5" fill="#1d1d1d">
        <text x="64" y="2238">10</text><text x="64" y="2267">10</text><text x="64" y="2293">10</text><text x="64" y="2321">10</text><text x="64" y="2346">10</text><text x="64" y="2372">10</text><text x="64" y="2398">10</text><text x="64" y="2425">10</text>
        <text x="95" y="2457">10</text><text x="121" y="2457">10</text><text x="147" y="2457">10</text><text x="173" y="2457">10</text><text x="199" y="2457">10</text><text x="225" y="2457">10</text><text x="251" y="2457">10</text><text x="277" y="2457">10</text>
      </g>
      <polyline vector-effect="non-scaling-stroke" fill="none" stroke="#1d1d1d" stroke-width="1.6" points="76,2425 97,2368 124,2370 149,2323 163,2335 175,2285 198,2296 229,2281 238,2325 267,2276"/>
      <polyline vector-effect="non-scaling-stroke" fill="none" stroke="#4fb3a6" stroke-width="1.6" points="76,2393 95,2365 104,2380 131,2330 152,2313 175,2310 183,2272 192,2320 218,2322 231,2300 246,2263 254,2300 267,2277"/>
      <g fill="#4fb3a6"><circle cx="95" cy="2365" r="1.6"/><circle cx="131" cy="2330" r="1.6"/><circle cx="152" cy="2313" r="1.6"/><circle cx="183" cy="2272" r="1.6"/><circle cx="218" cy="2322" r="1.6"/><circle cx="246" cy="2263" r="1.6"/><circle cx="267" cy="2277" r="1.6"/></g>
      <g fill="#1d1d1d"><circle cx="97" cy="2368" r="1.4"/><circle cx="149" cy="2323" r="1.4"/><circle cx="198" cy="2296" r="1.4"/><circle cx="238" cy="2325" r="1.4"/></g>
    </g>
  </svg>

  <div class="timeline__name" style="left:552px;top:213px;color:var(--teal-light)">Project 1</div>
  <p class="para abs" style="left:555px;top:268px;width:500px;font-size:13.5px;line-height:23px">Lorem ipsum dolor sit amet, consectetur adipiscing elit, sed do eiusmod tempor incididunt ut labore et dolore magna aliqua. Lorem ipsum dolor sit amet, consectetur adipiscing elit,</p>
  <div class="timeline__name" style="left:552px;top:355px;color:var(--ink)">Project 2</div>
  <p class="para abs" style="left:555px;top:410px;width:500px;font-size:13.5px;line-height:23px">Lorem ipsum dolor sit amet, consectetur adipiscing elit, sed do eiusmod tempor incididunt ut labore et dolore magna aliqua. Lorem ipsum dolor sit amet, consectetur adipiscing elit,</p>

  <div class="footer-band"></div>
  <svg class="steps" width="60" height="60"><rect x="0" y="0" width="20" height="60" fill="#2d7865"/><rect x="20" y="20" width="20" height="40" fill="#5a9a89"/><rect x="40" y="40" width="20" height="20" fill="#9cc4b8"/></svg>
  <div class="social" style="left:100px;top:612px"><span></span><span></span><span></span></div>
  <div class="phone" style="left:889px;top:610px"><svg width="14" height="14" viewBox="0 0 24 24"><path fill="#1d1d1d" d="M6.6 10.8a15 15 0 006.6 6.6l2.2-2.2c.3-.3.7-.4 1-.2 1.1.4 2.3.6 3.6.6.6 0 1 .4 1 1V20c0 .6-.4 1-1 1C10.6 21 3 13.4 3 4c0-.6.4-1 1-1h3.5c.6 0 1 .4 1 1 0 1.3.2 2.5.6 3.6.1.3 0 .7-.2 1z"/></svg>+(1) 555 014 2290</div>
  <svg class="abs" style="right:39px;bottom:0" width="40" height="40"><rect x="0" y="20" width="20" height="20" fill="#cfe2dc"/><rect x="20" y="0" width="20" height="40" fill="#9cc4b8"/></svg>
  <div class="page-no" style="width:39px;height:61px;padding-top:12px">06</div>
</section>

</body>
</html>
```